Pediatric Therapy Clinic Brochure

We need a Brochure for a new pediatric therapy clinic. The clinic offers occupational therapy, physical therapy, speech therapy and feeding therapy. We want a brochure for parents, doctors and medical professional. It should have a fun and inviting, but still professional feel. Should be kid focused, bright and colorful. All the text / wording is there and a rough layout. Now I need someone to tidy and jazz it up and make it look professional.

Target Market(s)

Parents, doctors, medical professional

Industry/Entity Type

Medical

Font styles to use
Serif
Sans Serif

Requirements
Must have
• Keep All the text with information about services the same. Logo on front. Pictures throughout (use any of the pictures provided) (try and match up with corresponding service) (pictures are labeled). Need to have Map and contact info
• Keep colors consistent with our logo
Nice to have
• Background, special effects. Make it look fancy and professional
Should not have
• Not so busy that is takes away from the text

```html
<!DOCTYPE html>
<html lang="en">
<head>
<meta charset="UTF-8">
<title>Sunridge Pediatric Therapy – Brochure</title>
<link href="https://fonts.googleapis.com/css2?family=Montserrat:wght@400;500;600;800&display=swap" rel="stylesheet">
<style>
  :root {
    --backdrop: #a4a4a4;
    --brand-blue: #1d6a9c;
    --brand-orange: #ec7a2a;
    --page-light: #f6f8fa;
    --page-mid: #e4e9ee;
    --back-light: #f4f4f4;
    --back-mid: #dedede;
  }
  * { margin: 0; padding: 0; box-sizing: border-box; }
  html, body {
    width: 1200px; height: 1200px; overflow: hidden;
    background: var(--backdrop);
    font-family: "Montserrat", Arial, sans-serif;
  }
  .canvas { position: relative; width: 1200px; height: 1200px; }

  .page {
    position: absolute; width: 760px; height: 540px; overflow: hidden;
    box-shadow: 0 6px 18px rgba(0,0,0,0.25);
  }
  .page--front {
    left: 60px; top: 40px;
    background: linear-gradient(160deg, var(--page-light) 0%, var(--page-mid) 100%);
  }
  .page--back {
    left: 380px; top: 620px;
    background: linear-gradient(200deg, var(--back-light) 0%, var(--back-mid) 100%);
  }

  .brand-name {
    position: absolute; color: var(--brand-blue);
    font-weight: 800; line-height: 1.02; letter-spacing: -0.5px;
    display: flex; align-items: center; gap: 10px;
  }
  .brand-name__dot {
    flex: none; border-radius: 50%; background: var(--brand-orange);
  }
  .page--front .brand-name { left: 50px; top: 60px; font-size: 40px; }
  .page--front .brand-name__dot { width: 22px; height: 22px; }
  .page--back .brand-name { left: 40px; top: 40px; font-size: 20px; }
  .page--back .brand-name__dot { width: 12px; height: 12px; }

  .service-list {
    position: absolute; list-style: none; color: var(--brand-blue);
    font-variant: small-caps; font-weight: 500; font-size: 13px; line-height: 1.35;
  }
  .service-list--first { left: 50px; top: 170px; }
  .service-list--second { left: 290px; top: 170px; }

  .photo {
    position: absolute;
  }
  .photo--children-row {
    left: 110px; top: 270px; width: 640px; height: 270px;
    background: linear-gradient(90deg, #e8c7ad 0%, #7cbf5a 30%, #f2a7c6 60%, #63c3c9 85%, #e9d6c4 100%);
    border-radius: 120px 120px 0 0;
    opacity: 0.85;
  }
  .photo--toddlers {
    left: 360px; top: 130px; width: 360px; height: 360px;
    background: radial-gradient(ellipse at 50% 55%, #eadfd6 0%, #c9d9b8 45%, #dcdcdc 80%, rgba(222,222,222,0) 100%);
  }
  .map-inset {
    position: absolute; left: 600px; top: 340px; width: 120px; height: 110px;
    background: #f7f5f2; box-shadow: 0 2px 6px rgba(0,0,0,0.25);
  }

  .about {
    position: absolute; left: 40px; top: 80px; width: 200px;
    color: var(--brand-blue); font-size: 9.6px; line-height: 1.42;
  }
  .contact { position: absolute; left: 40px; top: 400px; width: 260px; }
  .contact__title {
    color: var(--brand-blue); font-variant: small-caps;
    font-weight: 800; font-size: 16px; margin-bottom: 4px;
  }
  .contact__lines {
    list-style: none; color: var(--brand-orange);
    font-size: 10px; line-height: 1.45;
  }
</style>
</head>
<body>
<div class="canvas">

  <section class="page page--front" aria-label="Brochure front cover">
    <div class="brand-name"><span class="brand-name__dot"></span><span>Sunridge<br>Pediatric Therapy</span></div>
    <ul class="service-list service-list--first">
      <li>Speech Therapy</li>
      <li>Occupational Therapy</li>
      <li>Physical Therapy</li>
    </ul>
    <ul class="service-list service-list--second">
      <li>Feeding Therapy</li>
      <li>Sensory Integration Therapy</li>
      <li>Group Therapy</li>
    </ul>
    <div class="photo photo--children-row" role="img" aria-label="Photo of four smiling children lying in a row with their chins in their hands"></div>
  </section>

  <section class="page page--back" aria-label="Brochure back cover">
    <div class="brand-name"><span class="brand-name__dot"></span><span>Sunridge Pediatric Therapy</span></div>
    <p class="about">We are a team of highly trained pediatric therapists located in Cedar Springs. We are dedicated to helping children and adolescents along with their families with a full scope of therapy services, including occupational therapy, physical therapy, speech therapy, feeding therapy, sensory integration therapy, and group classes to meet the needs of all children. When you walk into our clinic you will see climbing walls, bikes, suspension swings, a trampoline and quiet areas where children are achieving complex and interdisciplinary skills while having fun! Our mission is to provide compassionate and high quality therapy services in an enriching and enjoyable environment where all children thrive! Contact us today and learn which therapy would be most appropriate for your child.</p>
    <div class="contact">
      <h2 class="contact__title">Contact Us!</h2>
      <ul class="contact__lines">
        <li>Sunridge Pediatric Therapy</li>
        <li>1870 W. Linden Ave. Suite 210</li>
        <li>Cedar Springs, AZ 85390</li>
        <li>555.014.2287</li>
        <li>hello@sunridgepeds.example</li>
        <li>Visit us online:</li>
        <li>www.sunridgepeds.example</li>
      </ul>
    </div>
    <div class="photo photo--toddlers" role="img" aria-label="Photo of two toddlers playing doctor with a stethoscope"></div>
    <div class="map-inset" role="img" aria-label="Small street map showing the clinic location"></div>
  </section>

</div>
</body>
</html>
```